Rehab/fitness Business card design

I need a design that promotes "A ready made base for runners". services include assessment, massage, physiotherapy, pilates, suspension training, kinesiotaping in any combination.
I would like to bring the design into my website, flyers etc

Target Market(s)

athletes from beginner to elite - any age, male and female

Industry/Entity Type

Shop

Contact Information for Business Card

Ready-Made-Base for Runners
17 Parvel Crescent, Hollowmere, Tauranga
021 847 3610
gwen.farrowby@quillmail.test

Logo Text

Requirements
Nice to have
• Blue colour theme

```html
<!DOCTYPE html>
<html lang="en">
<head>
<meta charset="utf-8">
<title>Ready-Made-Base for Runners – Business Card</title>
<link href="https://fonts.googleapis.com/css2?family=Quicksand:wght@500;600;700&display=swap" rel="stylesheet">
<style>
  :root {
    --backdrop: #2b2b2d;
    --blue-light: #2a8fde;
    --blue-deep: #1565b4;
    --text-blue: #1a8fd6;
    --white: #ffffff;
    --card-shadow: rgba(0, 0, 0, 0.45);
  }
  * { margin: 0; padding: 0; box-sizing: border-box; }
  html, body {
    width: 1200px;
    height: 900px;
    overflow: hidden;
    background: var(--backdrop);
    font-family: "Quicksand", sans-serif;
  }
  .canvas {
    position: relative;
    width: 1200px;
    height: 900px;
    display: flex;
    align-items: center;
    justify-content: center;
    gap: 40px;
  }
  .card {
    width: 540px;
    height: 309px;
    border-radius: 2px;
    box-shadow: 0 18px 40px var(--card-shadow);
    position: relative;
    overflow: hidden;
  }
  /* Front side */
  .card--front {
    background: linear-gradient(135deg, var(--blue-light) 0%, var(--blue-deep) 100%);
    display: flex;
    align-items: center;
    padding-left: 56px;
  }
  .brand {
    display: flex;
    align-items: center;
    gap: 14px;
  }
  .brand__dot {
    width: 34px;
    height: 34px;
    border-radius: 50%;
    flex: none;
  }
  .brand__name {
    font-weight: 700;
    line-height: 1;
    white-space: nowrap;
  }
  .card--front .brand__dot { background: var(--white); }
  .card--front .brand__name { color: var(--white); font-size: 38px; }

  /* Back side */
  .card--back {
    background: var(--white);
    color: var(--text-blue);
    display: flex;
    flex-direction: column;
    align-items: center;
    padding-top: 44px;
    text-align: center;
  }
  .card--back .brand__dot { background: var(--text-blue); width: 22px; height: 22px; }
  .card--back .brand__name { color: var(--text-blue); font-size: 24px; }
  .services {
    margin-top: 38px;
    font-size: 19px;
    font-weight: 600;
    line-height: 1.3;
    padding: 0 30px;
  }
  .contact {
    margin-top: 22px;
    font-size: 13px;
    font-weight: 500;
    line-height: 1.45;
    font-style: normal;
  }
</style>
</head>
<body>
  <main class="canvas">
    <section class="card card--front" aria-label="Card front">
      <div class="brand">
        <span class="brand__dot"></span>
        <span class="brand__name">Ready-Made-Base</span>
      </div>
    </section>

    <section class="card card--back" aria-label="Card back">
      <div class="brand">
        <span class="brand__dot"></span>
        <span class="brand__name">Ready-Made-Base</span>
      </div>
      <p class="services">assessment, massage, physiotherapy, pilates,<br>suspension training, kinesiotaping.</p>
      <address class="contact">
        Ready-Made-Base for Runners<br>
        17 Parvel Crescent, Hollowmere, Tauranga<br>
        021 847 3610<br>
        gwen.farrowby@quillmail.test
      </address>
    </section>
  </main>
</body>
</html>
```